WordPress Site Design and Code for Technology Consulting Startup

We need a WordPress design and code to a new site on Tallow Bay. We have the logo and colors ready. The site will be a brochure site with a CONTACT page that contains a form that the prospective client fills out. The other pages would be ABOUT / SERVICES (3 option drop-down) / SUPPORT. The site should be appropriate for an IT Consulting / IT Managed Services / IT Project Management services in the Chicago area.

Across small, medium, large businesses.

Technology, network infrastructure, IT.

Coded - Design and coding required

5+ page

• I prefer mid-modern / simple / art deco / minimalist.

```html
<!DOCTYPE html>
<html lang="en">
<head>
<meta charset="utf-8">
<title>Corvane — Technology Consulting</title>
<link href="https://fonts.googleapis.com/css2?family=Poppins:wght@400;500;600;700&display=swap" rel="stylesheet">
<style>
:root{
  --orange:#f47216;
  --teal:#1b8fb3;
  --navy:#0a2846;
  --navy-deep:#061a30;
  --ink:#141414;
  --muted:#444;
  --grey-band:#efefef;
  --line:#9a9a9a;
  --footer:#121212;
  --white:#fff;
}
*{margin:0;padding:0;box-sizing:border-box}
html,body{width:1200px;height:4713px;overflow:hidden}
body{font-family:'Poppins',sans-serif;color:var(--ink);background:var(--white);position:relative}
.abs{position:absolute}
section{position:absolute;left:0;width:1200px}
p{line-height:1.55}
.label{font-size:11px;font-weight:600;color:var(--orange);letter-spacing:.3px;text-transform:uppercase}
.label.teal{color:var(--teal)}
.body-text{font-size:12.5px;color:var(--muted);line-height:1.65}
.more{font-size:11.5px;font-weight:600;display:flex;align-items:center;gap:10px;text-transform:uppercase}
.more svg{width:44px;height:10px}
.btn-outline{position:absolute;border:2px solid #555;font-size:11px;font-weight:500;color:var(--orange);display:flex;align-items:center;justify-content:center;text-transform:uppercase;background:transparent}
.placeholder{position:absolute}

/* hero */
.hero{top:0;height:626px;background:radial-gradient(ellipse at 78% 40%,#14507a 0%,var(--navy) 45%,var(--navy-deep) 100%)}
.nav-rule{top:75px;left:0;width:1200px;height:1px;background:rgba(120,180,220,.35)}
.menu-icon{left:84px;top:26px;width:28px;height:20px}
.brand{font-weight:600;letter-spacing:1px}
.hero .brand{left:134px;top:30px;font-size:17px;color:var(--teal);display:flex;align-items:center;gap:7px}
.brand .dot{width:11px;height:11px;background:var(--orange)}
.nav-link{top:28px;font-size:11.5px;font-weight:500;color:var(--white);text-transform:uppercase}
.nav-link.active{color:var(--orange)}
.hero-kicker{left:134px;top:162px;font-size:13px;font-weight:500;color:var(--white)}
.hero-title{left:134px;top:196px;font-size:49px;font-weight:700;line-height:1.12;color:var(--orange);text-transform:uppercase}
.hero-title span{color:var(--teal);display:block}
.hero-copy{left:134px;top:322px;width:340px;font-size:12.5px;color:var(--white);line-height:1.65}
.hero-more{left:134px;top:449px;color:var(--orange)}
.hero-tab{top:543px;font-size:12px;color:#cfe2f0}
.hero-tab.active{color:var(--white);font-weight:500}
.hero-tab.active::before{content:"";position:absolute;left:0;top:-9px;width:150px;height:2px;background:var(--orange)}

/* about */
.about{top:626px;height:409px}
.section-head{font-size:31px;font-weight:700;line-height:1.35;text-transform:uppercase}
/* who */
.who{top:1035px;height:419px;background:var(--grey-band)}
/* services */
.services{top:1454px;height:842px}
.center{left:0;width:1200px;text-align:center}
.services-title{font-size:33px;font-weight:700;color:var(--orange)}
.card{position:absolute;width:245px;height:243px;border:1.5px solid #777;text-align:center}
.card svg{position:absolute;left:82px;top:26px;width:80px;height:80px}
.card h3{position:absolute;left:0;right:0;top:134px;font-size:16px;font-weight:600;line-height:1.3;text-transform:uppercase}
/* bold steps */
.steps{top:2296px;height:563px;background:var(--grey-band)}
.steps-title{font-size:30px;font-weight:700}
.tab-label{font-size:10px;color:#333}
.story{font-size:15px;font-weight:500;line-height:1.35}
.story-link{font-size:11px;font-weight:600;color:var(--teal);text-transform:uppercase}
.dot{position:absolute;width:18px;height:18px;border-radius:50%;background:#c9c9c9}
.dot.on{background:var(--orange)}
/* video */
.video{top:2859px;height:499px}
/* insights */
.insights{top:3358px;height:624px}
.insights-title{font-size:30px;font-weight:600}
.rule{position:absolute;height:1px;background:#555}
.cat{font-size:8.5px;font-weight:600}
.post-title{font-size:17px;font-weight:600;line-height:1.22}
.post-copy{font-size:12px;color:#333;line-height:1.6}
.meta{font-size:9.5px;color:#666}
/* cta */
.cta{top:3982px;height:338px;background:var(--orange)}
.cta h2{position:absolute;font-size:27px;font-weight:600;color:var(--white);text-align:center}
.cta .btn-outline{border-color:var(--white);color:var(--white)}
/* footer */
.footer{top:4320px;height:393px;background:var(--footer);color:var(--white)}
.footer .brand{font-size:22px;color:var(--teal);display:flex;align-items:center;gap:9px}
.subscribe-input{background:#3a3a3a;color:#bbb;font-size:11px;display:flex;align-items:center;padding-left:22px}
.subscribe-btn{background:var(--orange);color:var(--white);font-size:11px;font-weight:600;display:flex;align-items:center;justify-content:center}
.footer-link{top:4631px;font-size:11.5px;font-weight:500}
.social{width:20px;height:20px;border-radius:50%;background:var(--white)}
</style>
</head>
<body>

<!-- HERO -->
<section class="hero">
  <div class="placeholder" role="img" aria-label="Glowing circuit-board lines and a wireframe light bulb on deep blue" style="left:760px;top:90px;width:380px;height:430px;background:radial-gradient(circle at 55% 45%,rgba(70,200,240,.45) 0%,rgba(30,120,180,.15) 45%,rgba(0,0,0,0) 70%)"></div>
  <div class="abs nav-rule"></div>
  <svg class="abs menu-icon" viewBox="0 0 28 20"><g stroke="#fff" stroke-width="2.4"><line x1="0" y1="2" x2="28" y2="2"/><line x1="0" y1="10" x2="28" y2="10"/><line x1="0" y1="18" x2="28" y2="18"/></g></svg>
  <div class="abs brand"><span class="dot"></span>CORVANE</div>
  <div class="abs nav-link active" style="left:622px">Home</div>
  <div class="abs nav-link" style="left:690px">About Us</div>
  <div class="abs nav-link" style="left:783px">Services</div>
  <div class="abs nav-link" style="left:874px">Contact</div>
  <div class="abs nav-link" style="left:1037px">Explore</div>
  <svg class="abs" style="left:1112px;top:25px;width:20px;height:20px" viewBox="0 0 20 20"><circle cx="8" cy="8" r="6.5" fill="none" stroke="#fff" stroke-width="2"/><line x1="13" y1="13" x2="19" y2="19" stroke="#fff" stroke-width="2"/></svg>

  <div class="abs hero-kicker">Global Trade Summit</div>
  <h1 class="abs hero-title">Connecting<span>The World</span></h1>
  <p class="abs hero-copy">Lorem ipsum dolor sit amet, consectetur adipiscing elit, sed do eiusmod tempor incididunt ut labore et dolore magna aliqua. Quis ipsum suspendisse ultrices gravida. Risus commodo viverra maecenas accumsan lacus vel facilisis.</p>
  <div class="abs more hero-more">Learn More <svg viewBox="0 0 44 10"><line x1="0" y1="5" x2="40" y2="5" stroke="#f47216" stroke-width="1.5"/><path d="M36 1l6 4-6 4" fill="none" stroke="#f47216" stroke-width="1.5"/></svg></div>

  <div class="abs hero-tab" style="left:128px">Customer Love</div>
  <div class="abs hero-tab" style="left:348px">M &amp; A Report</div>
  <div class="abs hero-tab active" style="left:530px">Global Trade Summit</div>
  <div class="abs hero-tab" style="left:816px">Factory of the Future</div>
</section>

<!-- ABOUT -->
<section class="about">
  <div class="abs label teal" style="left:134px;top:48px">About Us</div>
  <h2 class="abs section-head" style="left:134px;top:70px">Redefining Enterprise<br>Communication.</h2>
  <p class="abs body-text" style="left:134px;top:170px;width:380px">Lorem ipsum dolor sit amet, consectetur adipiscing elit, sed do eiusmod tempor incididunt ut labore et dolore magna aliqua. Quis ipsum suspendisse ultrices gravida. Risus commodo viverra maecenas accumsan lacus vel facilisis. Lorem ipsum dolor sit amet, consectetcommodo viverra maecenas accumsan lacus vel facilisis..</p>
  <div class="abs more" style="left:134px;top:315px;color:var(--orange)">Know More <svg viewBox="0 0 44 10"><line x1="0" y1="5" x2="40" y2="5" stroke="#f47216" stroke-width="1.5"/><path d="M36 1l6 4-6 4" fill="none" stroke="#f47216" stroke-width="1.5"/></svg></div>
  <div class="placeholder" role="img" aria-label="Photo of a smiling consultant meeting a client at a table" style="left:609px;top:36px;width:406px;height:333px;background:linear-gradient(135deg,#8fa08a 0%,#c7cfc6 45%,#7c8d9b 100%)"></div>
</section>

<!-- WHO WE ARE -->
<section class="who">
  <div class="placeholder" role="img" aria-label="Photo of a business team discussing documents in an office" style="left:134px;top:40px;width:406px;height:333px;background:linear-gradient(135deg,#e6e6e3 0%,#c9c6c0 50%,#3a3a3d 100%)"></div>
  <div class="abs label" style="left:609px;top:60px">Who We Are</div>
  <h2 class="abs section-head" style="left:609px;top:80px">Get Expexrty Advice &amp;<br>Start Your Business</h2>
  <p class="abs body-text" style="left:609px;top:180px;width:380px">Lorem ipsum dolor sit amet, consectetur adipiscing elit, sed do eiusmod tempor incididunt ut labore et dolore magna aliqua. Quis ipsum suspendisse ultrices gravida. Risus commodo viverra maecenas accumsan lacus vel facilisis. Lorem ipsum dolor sit amet, consectetcommodo viverra maecenas accumsan lacus vel facilisis..</p>
  <div class="abs more" style="left:609px;top:325px;color:var(--teal)">Know More <svg viewBox="0 0 44 10"><line x1="0" y1="5" x2="40" y2="5" stroke="#1b8fb3" stroke-width="1.5"/><path d="M36 1l6 4-6 4" fill="none" stroke="#1b8fb3" stroke-width="1.5"/></svg></div>
</section>

<!-- SERVICES -->
<section class="services">
  <div class="abs center label teal" style="top:48px">Our Services</div>
  <h2 class="abs center services-title" style="top:68px">WHAT INDUSTRY WE SERVE</h2>
  <p class="abs body-text" style="left:274px;top:124px;width:652px;text-align:center;color:#222">Lorem ipsum dolor sit amet, consectetur adipiscing elit, sed do eiusmod tempor incididunt ut labore et dolore magna aliqua. Quis ipsum suspendisse ultrices gravida. Risus commodo viverra maecenas accumsan lacus vel facilisis.</p>

  <div class="card" style="left:203px;top:220px">
    <svg viewBox="0 0 80 80" fill="none" stroke="#1b8fb3" stroke-width="2.2"><path d="M40 8L8 22l32 14 32-14z"/><path d="M20 28v14c0 6 40 6 40 0V28"/><path d="M66 25v14"/><rect x="12" y="48" width="56" height="16" rx="8"/><path d="M36 64v10l4-3 4 3V64"/></svg>
    <h3>Education</h3>
  </div>
  <div class="card" style="left:477px;top:220px">
    <svg viewBox="0 0 80 80" fill="none" stroke="#1b8fb3" stroke-width="2.2"><path d="M40 42l-10-10a6 6 0 018-8l2 2 2-2a6 6 0 018 8z"/><path d="M6 48l14 14h26l10-8"/><path d="M74 32L60 18H34l-10 8"/><circle cx="40" cy="34" r="22" stroke-dasharray="4 5"/></svg>
    <h3>Health</h3>
  </div>
  <div class="card" style="left:752px;top:220px">
    <svg viewBox="0 0 80 80" fill="none" stroke="#1b8fb3" stroke-width="2.2"><rect x="6" y="8" width="40" height="30"/><rect x="11" y="13" width="30" height="20"/><path d="M22 38v8h8"/><path d="M34 46h30c8 0 12 26 4 26-5 0-7-8-10-8H44c-3 0-5 8-10 8-8 0-4-26 0-26z"/><path d="M44 54v8M40 58h8"/><circle cx="58" cy="56" r="2"/><circle cx="62" cy="61" r="2"/></svg>
    <h3>Gaming</h3>
  </div>
  <div class="card" style="left:203px;top:490px">
    <svg viewBox="0 0 80 80" fill="none" stroke="#1b8fb3" stroke-width="2.2"><path d="M30 20l3-8h14l3 8 8 3v10"/><path d="M22 33V23l8-3"/><rect x="14" y="33" width="52" height="34"/><path d="M8 67h64"/><path d="M32 44l-6 6 6 6M48 44l6 6-6 6M43 42l-6 16"/></svg>
    <h3>IT Service</h3>
  </div>
  <div class="card" style="left:477px;top:490px">
    <svg viewBox="0 0 80 80" fill="none" stroke="#1b8fb3" stroke-width="2.2"><rect x="12" y="8" width="56" height="66"/><path d="M12 34h56"/><path d="M12 34c0 6 56 6 56 0"/><path d="M28 16h4l4 12h14l3-8H34"/><rect x="20" y="46" width="14" height="28"/><rect x="42" y="46" width="18" height="14"/></svg>
    <h3>Retail</h3>
  </div>
  <div class="card" style="left:752px;top:490px">
    <svg viewBox="0 0 80 80" fill="none" stroke="#1b8fb3" stroke-width="2.2"><rect x="6" y="6" width="68" height="68" rx="3"/><path d="M6 16h68"/><circle cx="12" cy="11" r="1.5"/><circle cx="17" cy="11" r="1.5"/><circle cx="40" cy="38" r="14"/><path d="M36 31l10 7-10 7z"/><path d="M14 64h52"/><circle cx="28" cy="64" r="3"/></svg>
    <h3>Media<br>&amp;<br>Entertainment</h3>
  </div>

  <div class="btn-outline" style="left:508px;top:765px;width:183px;height:43px">View All Category</div>
</section>

<!-- BOLD STEPS -->
<section class="steps">
  <div class="abs label" style="left:134px;top:50px">About Us</div>
  <h2 class="abs steps-title" style="left:134px;top:70px">Bold steps forward.</h2>
  <p class="abs" style="left:134px;top:123px;width:330px;font-size:12px;line-height:1.7">See how we've helped ambitious clients achieve extraordinary outcomes.</p>
  <div class="abs tab-label" style="left:134px;top:185px">Featured client sucess story</div>
  <div class="abs" style="left:134px;top:205px;width:186px;height:2px;background:var(--teal)"></div>
  <div class="abs story" style="left:150px;top:230px;width:160px">Sales blueprint put IT services Co.'s growth back on track.</div>
  <div class="abs story-link" style="left:150px;top:342px">Read Story ▸</div>
  <div class="abs tab-label" style="left:340px;top:185px">How we helped</div>
  <div class="abs" style="left:340px;top:209px;width:181px;height:160px;border:1.5px solid #888;background:var(--white)"></div>
  <div class="abs story" style="left:354px;top:230px">Agile Enterprise.</div>
  <div class="abs story-link" style="left:354px;top:342px">View Offering ▸</div>
  <div class="placeholder" role="img" aria-label="Photo of a car chassis on a factory assembly line" style="left:587px;top:36px;width:428px;height:351px;background:linear-gradient(160deg,#9aa3ab 0%,#5b6570 45%,#2d333a 75%,#a68a6b 100%)"></div>
  <div class="dot" style="left:560px;top:424px"></div>
  <div class="dot on" style="left:590px;top:424px"></div>
  <div class="dot" style="left:620px;top:424px"></div>
  <div class="btn-outline" style="left:508px;top:486px;width:183px;height:44px">View All Client Result</div>
</section>

<!-- VIDEO -->
<section class="video">
  <div class="placeholder" role="img" aria-label="Video still of three colleagues talking around a coffee table" style="left:0;top:0;width:1200px;height:499px;background:linear-gradient(100deg,#2f3742 0%,#7a6a5c 35%,#4a3136 55%,#c8c3bb 80%,#8fa6c2 100%)"></div>
  <svg class="abs" style="left:558px;top:204px;width:82px;height:92px" viewBox="0 0 82 92"><path d="M0 0l82 46L0 92z" fill="#e8161b"/></svg>
</section>

<!-- INSIGHTS -->
<section class="insights">
  <div class="rule" style="left:183px;top:48px;width:250px"></div>
  <h2 class="abs center insights-title" style="top:26px">Our Latest Insights</h2>
  <div class="rule" style="left:763px;top:48px;width:252px"></div>

  <div class="placeholder" role="img" aria-label="Photo of a paved path through a green forest" style="left:183px;top:99px;width:408px;height:238px;background:linear-gradient(180deg,#2f4a22 0%,#5f8a3d 50%,#7b7466 100%)"></div>
  <div class="abs cat" style="left:183px;top:348px">Sustainability &amp; Responsibility</div>
  <div class="abs post-title" style="left:183px;top:366px;width:380px">Voluntary Carbon Markets in 2023: A Bumpy Road Behind, Crossroads Ahead</div>
  <p class="abs post-copy" style="left:183px;top:440px;width:360px">The markets for carbon credits will either rationalize or be stifled by uncertainty and complexity.</p>
  <div class="abs meta" style="left:183px;top:506px">Brief</div>
  <svg class="abs" style="left:576px;top:502px;width:12px;height:16px" viewBox="0 0 12 16"><path d="M1 1h10v14l-5-4-5 4z" fill="none" stroke="#111" stroke-width="1.6"/></svg>

  <div class="abs" style="left:600px;top:99px;width:1px;height:430px;background:#777"></div>

  <div class="placeholder" role="img" aria-label="Photo of an engineer inspecting metal parts in a workshop" style="left:609px;top:99px;width:406px;height:238px;background:linear-gradient(135deg,#c9cbc9 0%,#7f8587 50%,#3a3c40 100%)"></div>
  <div class="abs cat" style="left:609px;top:348px">Procurement</div>
  <div class="abs post-title" style="left:609px;top:366px;width:400px">Circular Transformation of Industries: Unlocking New Value in a Resource-Constrained World</div>
  <p class="abs post-copy" style="left:609px;top:440px;width:360px">Circularity initiatives to date have shown that isolated efforts are not enough.</p>
  <div class="abs meta" style="left:609px;top:506px">Global Trade Summit</div>
  <svg class="abs" style="left:1002px;top:502px;width:12px;height:16px" viewBox="0 0 12 16"><path d="M1 1h10v14l-5-4-5 4z" fill="none" stroke="#111" stroke-width="1.6"/></svg>

  <div class="btn-outline" style="left:508px;top:549px;width:183px;height:44px">See All Insights</div>
</section>

<!-- CTA -->
<section class="cta">
  <h2 style="left:80px;width:516px;top:100px">What can we help you achieve?</h2>
  <div class="btn-outline" style="left:245px;top:194px;width:183px;height:44px">Let's Get To Work</div>
  <div class="abs" style="left:600px;top:28px;width:1.5px;height:283px;background:rgba(255,255,255,.7)"></div>
  <h2 style="left:610px;width:510px;top:100px">Where will your career take you?</h2>
  <div class="btn-outline" style="left:774px;top:186px;width:183px;height:43px">Come Find Out</div>
</section>

<!-- FOOTER -->
<section class="footer">
  <p class="abs" style="left:183px;top:62px;width:420px;font-size:12.5px;line-height:1.6">Stay ahead in a rapidly changing world. Subscribe to Corvane Insights, our monthly look at the critical issues facing global businesses.</p>
  <div class="abs subscribe-input" style="left:669px;top:70px;width:244px;height:49px">ENTER YOUR EMAIL</div>
  <div class="abs subscribe-btn" style="left:929px;top:70px;width:86px;height:49px">SUBMIT</div>
  <div class="abs" style="left:671px;top:145px;width:16px;height:16px;background:var(--white)"></div>
  <p class="abs" style="left:702px;top:140px;width:300px;font-size:11px">*I have read the Privacy Policy and agree to its terms.</p>

  <div class="abs brand" style="left:183px;top:210px"><span class="dot" style="width:14px;height:14px"></span>CORVANE</div>
  <div class="abs" style="left:677px;top:217px;display:flex;gap:18px">
    <span class="social"></span><span class="social"></span><span class="social"></span><span class="social"></span><span class="social"></span>
  </div>

  <div class="abs footer-link" style="left:183px;top:311px">HOME</div>
  <div class="abs footer-link" style="left:252px;top:311px">ABOUT US</div>
  <div class="abs footer-link" style="left:346px;top:311px">SERVICES</div>
  <div class="abs footer-link" style="left:435px;top:311px">CONTACT</div>
  <div class="abs" style="left:183px;top:342px;font-size:11px;color:#bbb">© 2023 CORVANE. All Rights Reserved.</div>
</section>

</body>
</html>
```